Catholic composer needs poster for new musical, "THE STONE AND THE VIGIL, the Harvest Musical"

We need a dynamic poster for "The Stone and the Vigil," a new musical written for Catholic dinner theater. We need you to create an iconic design like you see in posters for classic musicals, like "Rosa Calendula," Lantern of the Harbour," or "Gilded." In our musical, “fire” represents the Holy Spirit, who showers man with his merciful love.

Miraculous events occur. A mighty wind from heaven fills the house. Tongues of fire appear over their heads. They speak in other tongues that are understandable by all present. They are emboldened to go out and tell the Good News to the world, despite the risks associated with evangelizing this fledgling religion. They exclaim, “Lord, you will show us the path to life.”

Target Market(s)

The audience is adult members of Catholic churches. But don't make the design look too "churchy."

Requirements
Must have
• Photoshop or Illustrated file with layers, or vector format.
Should not have
• Really don't want photos.

```html
<!DOCTYPE html>
<html lang="en">
<head>
<meta charset="utf-8">
<title>The Stone and the Vigil — The Harvest Musical</title>
<link rel="stylesheet" href="https://fonts.googleapis.com/css2?family=Oswald:wght@500;700&family=Pinyon+Script&family=Open+Sans:wght@400;600&display=swap">
<style>
  :root {
    --deep-red: #5a0d07;
    --mid-red: #8e1c0a;
    --ember: #c8400f;
    --glow: #ffcf5a;
    --gold-light: #ffe39a;
    --gold: #f2b233;
    --gold-dark: #c9761a;
    --cream: #fff4dc;
    --line: #d99a3a;
  }
  * { margin: 0; padding: 0; box-sizing: border-box; }
  html, body { width: 849px; height: 1200px; overflow: hidden; background: var(--deep-red); }
  .poster {
    position: relative;
    width: 849px;
    height: 1200px;
    overflow: hidden;
    background:
      radial-gradient(circle at 50% 28%, #ffb347 0%, #e9661a 14%, var(--ember) 26%, var(--mid-red) 46%, var(--deep-red) 78%, #3d0804 100%);
    font-family: "Open Sans", sans-serif;
    color: var(--cream);
    text-align: center;
  }
  .hero-art {
    position: absolute;
    left: 214px;
    top: 30px;
    width: 420px;
    height: 560px;
    border-radius: 50% 50% 46% 46%;
    background:
      radial-gradient(ellipse at 50% 40%, #fff3b0 0%, var(--glow) 18%, #f08a22 40%, rgba(200,64,15,0.6) 62%, rgba(142,28,10,0) 78%);
  }
  .title {
    position: absolute;
    left: 0;
    width: 100%;
    top: 585px;
    font-family: "Oswald", sans-serif;
    font-weight: 700;
    font-size: 78px;
    line-height: 66px;
    letter-spacing: 1px;
    text-transform: uppercase;
    background: linear-gradient(180deg, var(--gold-light) 0%, var(--gold) 55%, var(--gold-dark) 100%);
    -webkit-background-clip: text;
    background-clip: text;
    color: transparent;
  }
  .subtitle {
    position: absolute;
    left: 0; width: 100%;
    top: 722px;
    font-family: "Oswald", sans-serif;
    font-weight: 500;
    font-size: 34px;
    letter-spacing: 1px;
    color: var(--cream);
  }
  .tagline {
    position: absolute;
    left: 0; width: 100%;
    top: 790px;
    font-family: "Oswald", sans-serif;
    font-weight: 500;
    font-size: 30px;
    line-height: 34px;
    color: var(--gold);
  }
  .author {
    position: absolute;
    left: 0; width: 100%;
    top: 862px;
    font-family: "Oswald", sans-serif;
    font-size: 15px;
    letter-spacing: 1px;
    color: var(--gold);
  }
  .quote {
    position: absolute;
    left: 0; width: 100%;
    top: 890px;
    font-family: "Pinyon Script", cursive;
    font-size: 40px;
    color: var(--cream);
  }
  .details {
    position: absolute;
    left: 396px;
    top: 972px;
    width: 260px;
    list-style: none;
    text-align: left;
    font-size: 15px;
    color: var(--cream);
  }
  .details li {
    height: 38px;
    display: flex;
    align-items: flex-end;
    gap: 6px;
  }
  .details li::after {
    content: "";
    flex: 1;
    border-bottom: 1px dotted var(--cream);
    margin-bottom: 4px;
  }
  .site {
    position: absolute;
    left: 85px;
    right: 85px;
    top: 1144px;
    display: flex;
    align-items: center;
    gap: 16px;
    font-size: 19px;
    font-weight: 600;
    letter-spacing: 3px;
    color: var(--gold);
  }
  .site::before, .site::after {
    content: "";
    flex: 1;
    height: 2px;
    background: var(--line);
  }
</style>
</head>
<body>
<main class="poster">
  <div class="hero-art" role="img" aria-label="Glowing heart wrapped in a crown of thorns, engulfed in flames and topped by a small cross"></div>

  <h1 class="title">The Stone and<br>the Vigil</h1>
  <p class="subtitle">THE HARVEST MUSICAL</p>
  <p class="tagline">A NEW MUSICAL FOR<br>CATHOLIC DINNER THEATER</p>
  <p class="author">BY ELIAS MARWOOD</p>
  <p class="quote">“Set us afire with your merciful love.”</p>

  <ul class="details">
    <li>Where:</li>
    <li>Date:</li>
    <li>Time:</li>
    <li>Ticket Prices:</li>
  </ul>

  <p class="site">www.thestoneandthevigil.com</p>
</main>
</body>
</html>
```